School Poster and Prompt Design

I would like posters created for each of our school values (from the attached Way of Working document). In these posters I would like our logo, and some graphics or pictures - you can use the strategic plan attached for some examples.

I would also like a Code of Conduct Prompt for teachers and students (smaller design that can be used as a sticker for a laptop) based on the attached Tolworth Vale Essentials document. I have also attached a photo example, which we quite like that can be used for a base. This document is called example classroom management prompts.

Target Market(s)

School and students

Requirements
Must have
• Logo built into the design
Our school motto at the bottom 'Strive to Accomplish'
Design that incorporates elements that relate to each of the values.
Design that looks and feels like the example. In our school colours.
Nice to have
• Posters - Easy to read and understand from a distance.
Prompt - Easy to read and understand if turned into a sticker for a laptop.

```html
<!DOCTYPE html>
<html lang="en">
<head>
<meta charset="utf-8">
<title>Our Values – Common Sense</title>
<link rel="stylesheet" href="https://fonts.googleapis.com/css2?family=Archivo+Black&family=Roboto+Condensed:wght@400&family=Arimo:wght@400&display=swap">
<style>
  :root {
    --backdrop: #f1f1ef;
    --paper: #ffffff;
    --navy: #122062;
    --navy-deep: #0e1a55;
    --ocean: #0d6aa8;
    --cyan: #1fb4e0;
    --white: #ffffff;
    --photo-light: #9a9fcf;
    --photo-mid: #6d72b0;
  }
  * { box-sizing: border-box; margin: 0; padding: 0; }
  html, body { width: 1200px; height: 900px; overflow: hidden; }
  body { background: var(--backdrop); position: relative; }

  .poster {
    position: absolute; left: 296px; top: 20px;
    width: 609px; height: 860px;
    background: var(--paper);
    box-shadow: 0 4px 14px rgba(0,0,0,0.18);
  }
  .value-panel {
    position: absolute; left: 32px; top: 31px;
    width: 546px; height: 743px;
    background: linear-gradient(100deg, var(--navy-deep) 0%, var(--navy) 45%, var(--ocean) 100%);
    overflow: hidden;
  }
  .student-photo {
    position: absolute; left: 0; top: 0; width: 546px; height: 270px;
    background:
      radial-gradient(ellipse at 70% 60%, var(--photo-light) 0%, transparent 60%),
      linear-gradient(90deg, var(--navy) 0%, var(--photo-mid) 40%, var(--photo-light) 75%, var(--photo-mid) 100%);
  }
  .school-name {
    position: absolute; left: 30px; top: 40px;
    display: flex; align-items: center; gap: 10px;
    font-family: "Roboto Condensed", sans-serif; font-weight: 400;
    font-size: 20px; line-height: 1.1; color: var(--white); white-space: nowrap;
  }
  .school-name .dot {
    flex: none; width: 20px; height: 20px; border-radius: 50%; background: var(--white);
  }
  .values-label {
    position: absolute; left: 10px; right: 10px; top: 282px;
    display: flex; align-items: center; gap: 8px;
    font-family: "Roboto Condensed", sans-serif; font-weight: 400; font-size: 35px;
    color: var(--white); white-space: nowrap;
  }
  .values-label::before, .values-label::after {
    content: ""; flex: 1; height: 1px; background: var(--white);
  }
  .value-name {
    position: absolute; left: 0; right: 0; top: 332px;
    text-align: center; font-family: "Archivo Black", sans-serif; font-weight: 400;
    font-size: 64px; line-height: 64px; color: var(--cyan);
  }
  .value-tagline {
    position: absolute; left: 0; right: 0; top: 466px;
    text-align: center; font-family: "Roboto Condensed", sans-serif; font-weight: 400;
    font-size: 34px; color: var(--white);
  }
  .behaviour-list {
    position: absolute; left: 72px; top: 528px; width: 401px; height: 142px;
    border: 1px solid var(--white); list-style: none;
    padding: 18px 0 0 22px;
    font-family: "Arimo", sans-serif; font-size: 18.5px; line-height: 27px; color: var(--white);
  }
  .behaviour-list li { position: relative; padding-left: 12px; }
  .behaviour-list li::before {
    content: ""; position: absolute; left: 0; top: 12px;
    width: 4px; height: 4px; border-radius: 50%; background: var(--cyan);
  }
  .motto-bar {
    position: absolute; left: 32px; top: 786px; width: 492px; height: 43px;
    background: var(--navy);
    font-family: "Roboto Condensed", sans-serif; font-weight: 400; font-size: 26px; line-height: 43px;
    color: var(--cyan); text-align: right; padding-right: 22px;
  }
  .motto-square {
    position: absolute; left: 535px; top: 786px; width: 43px; height: 43px;
    background: var(--navy);
  }
</style>
</head>
<body>
  <main class="poster">
    <section class="value-panel">
      <div class="student-photo" role="img" aria-label="Photo of two smiling students in school uniform"></div>
      <div class="school-name"><span class="dot"></span><span>Tolworth Vale High School</span></div>
      <h2 class="values-label">OUR VALUES:</h2>
      <h1 class="value-name">Common<br>Sense</h1>
      <p class="value-tagline">In all our decision-making</p>
      <ul class="behaviour-list">
        <li>Show sensible behaviour</li>
        <li>Accept the outcome of your decisions</li>
        <li>Follow all school policies</li>
        <li>Ensure your own and others’ safety</li>
      </ul>
    </section>
    <footer>
      <div class="motto-bar">Strive to accomplish</div>
      <div class="motto-square" aria-hidden="true"></div>
    </footer>
  </main>
</body>
</html>
```